Retiros Silencio

I want a Catholic flyer, with the Virgen Mary showing aiding, praying, and Jesus carrying the cross, to invite people to a silent retreat. The retreats are monthly. For women, they are Feb. 21, March 21, etc (every third Saturday), and for men they are Feb. 28, March 28, etc (every fourth Saturday). I want each month date to show for both women and men. Our logo should be in there, which is similar to the Holy family icon attached. Also, show that cost is $80, and the place for the retreats is Casa Alborada, 4187 Juniper Ct, Falls Church, VA and for more information to contact, for women 540-555-0147 and for men 571-555-0182. I will use the flyer for around 4 x 6 or 3 x 5 postcard. Organizers are: Nidos de Valle Claro. The flyer needs to be in spanish "RETIROS EN SILENCIO" and the months should be labeled in Spanish too.

```html
<!DOCTYPE html>
<html lang="es">
<head>
<meta charset="utf-8">
<title>Retiros en Silencio</title>
<link href="https://fonts.googleapis.com/css2?family=Alegreya+Sans+SC:wght@700;800;900&family=Poppins:wght@400;600;700&family=Crimson+Text:wght@400&display=swap" rel="stylesheet">
<style>
  :root{
    --page:#adadad;
    --gold:#ffc21a;
    --gold-light:#fff06a;
    --gold-deep:#f0a400;
    --ink-dark:#3a0d05;
    --white:#ffffff;
    --sky-top:#e8742a;
    --glow:#ffd83a;
    --ember:#a82f0c;
    --rust:#7c2208;
    --night:#250805;
  }
  *{margin:0;padding:0;box-sizing:border-box}
  html,body{width:956px;height:1200px;overflow:hidden;background:var(--page)}
  .flyer{
    position:absolute;left:78px;top:0;width:800px;height:1200px;overflow:hidden;
    background:linear-gradient(180deg,var(--sky-top) 0%,#d8541e 22%,var(--ember) 34%,var(--rust) 50%,#521305 75%,var(--night) 100%);
    font-family:"Poppins",sans-serif;color:var(--white);
  }
  .sky-scene{
    position:absolute;left:0;top:0;width:800px;height:340px;
    background:
      radial-gradient(ellipse 220px 150px at 400px 0px,var(--glow) 0%,rgba(255,200,50,.6) 45%,rgba(255,160,40,0) 100%),
      radial-gradient(ellipse 520px 90px at 400px 250px,rgba(240,140,110,.55) 0%,rgba(240,140,110,0) 100%),
      linear-gradient(180deg,rgba(0,0,0,0) 60%,rgba(150,40,10,.6) 100%);
  }
  .organizer-mark{
    position:absolute;left:343px;top:41px;width:114px;height:161px;
    background:linear-gradient(180deg,#8a5a2a,#5a3a1a);
    border:4px solid #6b5a3a;
    display:flex;flex-direction:column;align-items:center;justify-content:center;gap:8px;
    font-family:"Poppins",sans-serif;font-weight:600;font-size:13px;line-height:1.25;text-align:center;color:var(--gold);
    padding:6px;
  }
  .organizer-mark .dot{width:14px;height:14px;border-radius:50%;background:var(--gold)}
  .crowd-scene{
    position:absolute;left:0;top:220px;width:800px;height:140px;
    background:linear-gradient(180deg,rgba(150,40,10,0) 0%,rgba(160,42,10,.85) 45%,var(--ember) 100%);
  }
  .crowd-foot{
    position:absolute;left:40px;bottom:0;width:720px;height:150px;
    background:linear-gradient(180deg,rgba(30,5,3,0) 0%,rgba(30,5,3,.45) 100%);
  }
  .title-main,.title-sub{
    position:absolute;left:0;width:800px;text-align:center;
    font-family:"Alegreya Sans SC",sans-serif;font-weight:900;letter-spacing:1px;
  }
  .title-main{
    top:300px;font-size:168px;line-height:1;
    background:linear-gradient(180deg,var(--gold-deep) 0%,var(--gold-light) 50%,var(--gold) 100%);
    -webkit-background-clip:text;background-clip:text;color:transparent;
    filter:drop-shadow(0 3px 2px rgba(60,10,0,.8));
  }
  .title-sub{top:455px;font-size:124px;line-height:1;color:var(--white);filter:drop-shadow(0 3px 3px rgba(60,10,0,.7))}
  .banner-monthly{
    position:absolute;left:70px;top:586px;width:643px;height:66px;
    background:linear-gradient(90deg,var(--gold) 0%,var(--gold-light) 50%,var(--gold) 100%);
    border-radius:4px;box-shadow:0 3px 8px rgba(0,0,0,.4);
    display:flex;align-items:center;justify-content:center;
    font-family:"Alegreya Sans SC",sans-serif;font-weight:800;font-size:46px;color:var(--ink-dark);letter-spacing:1px;
  }
  .schedule{
    position:absolute;top:708px;width:263px;height:162px;
    border:1px solid var(--gold);border-radius:10px;text-align:center;
  }
  .schedule.women{left:91px}
  .schedule.men{left:405px}
  .schedule-tab{
    position:absolute;left:8px;top:-24px;width:244px;height:47px;border-radius:5px;
    background:var(--gold);color:#8a1a05;display:flex;align-items:center;justify-content:center;
    font-family:"Alegreya Sans SC",sans-serif;font-weight:800;font-size:30px;
  }
  .schedule-body{position:absolute;left:0;top:28px;width:100%;font-size:23px;line-height:1.22}
  .schedule-body b{color:var(--gold);font-weight:700}
  .schedule-body small{display:block;font-size:17px}
  .cost{
    position:absolute;left:135px;top:896px;width:460px;height:60px;background:var(--white);border-radius:12px;
  }
  .cost-label{
    position:absolute;left:155px;top:896px;height:60px;display:flex;align-items:center;
    font-family:"Alegreya Sans SC",sans-serif;font-weight:800;font-size:48px;color:var(--ink-dark);
  }
  .cost-price{
    position:absolute;left:542px;top:884px;font-family:"Poppins",sans-serif;font-weight:700;font-size:78px;line-height:1;
    color:var(--gold);-webkit-text-stroke:4px #3a0d05;paint-order:stroke fill;
  }
  .cost-price sup{font-size:38px;vertical-align:30px}
  .rule{position:absolute;left:155px;width:490px;height:1px;background:linear-gradient(90deg,rgba(255,194,26,0),var(--gold),rgba(255,194,26,0))}
  .rule.top{top:982px}
  .rule.bottom{top:1035px}
  .venue{
    position:absolute;left:0;top:993px;width:800px;text-align:center;
    font-family:"Crimson Text",serif;font-size:22px;
  }
  .venue svg{vertical-align:-3px;margin-right:6px}
  .contact-title{position:absolute;left:0;top:1052px;width:800px;text-align:center;font-weight:600;font-size:24px}
  .contact{position:absolute;top:1090px;}
  .contact.women{left:186px}
  .contact.men{left:431px}
  .contact-label{font-family:"Alegreya Sans SC",sans-serif;font-weight:800;font-size:18px;color:var(--gold);line-height:1}
  .contact-phone{font-weight:700;font-size:21px;line-height:1.3}
  .contact-phone svg{vertical-align:0;margin-right:4px}
  .divider{position:absolute;left:403px;top:1092px;width:1px;height:44px;background:var(--white)}
</style>
</head>
<body>
<div class="flyer">
  <div class="sky-scene" role="img" aria-label="Cielo dorado con nubes y la figura de Cristo en la luz"></div>
  <div class="crowd-scene" role="img" aria-label="Siluetas de fieles con los brazos alzados"></div>
  <div class="crowd-foot" role="img" aria-label="Siluetas tenues de fieles al pie del volante"></div>

  <div class="organizer-mark"><span class="dot"></span>Nidos de Valle Claro</div>

  <h1 class="title-main">RETIROS</h1>
  <h2 class="title-sub">EN SILENCIO</h2>

  <div class="banner-monthly">Los retiros son mensuales</div>

  <section class="schedule women">
    <div class="schedule-tab">PARA MUJERES</div>
    <p class="schedule-body">se realizan el<br><b>21 de febrero</b><br>el <b>21 de marzo</b><small>(cada tercer sábado)</small></p>
  </section>
  <section class="schedule men">
    <div class="schedule-tab">PARA HOMBRES</div>
    <p class="schedule-body">se realizan el<br><b>28 de febrero</b><br>el <b>28 de marzo</b><small>(cada cuarto sábado)</small></p>
  </section>

  <div class="cost"></div>
  <div class="cost-label">El costo es de</div>
  <div class="cost-price"><sup>$</sup>80</div>

  <div class="rule top"></div>
  <p class="venue"><svg width="16" height="18" viewBox="0 0 16 18"><path d="M8 1a5 5 0 0 0-5 5c0 4 5 8 5 8s5-4 5-8a5 5 0 0 0-5-5z" fill="none" stroke="#ffc21a" stroke-width="2"/><circle cx="8" cy="6" r="1.8" fill="#ffc21a"/><path d="M2 16h12" stroke="#ffc21a" stroke-width="2"/></svg>Casa Alborada, 4187 Juniper Ct, Falls Church, VA.</p>
  <div class="rule bottom"></div>

  <p class="contact-title">Para más información</p>
  <div class="contact women">
    <div class="contact-label">PARA MUJERES</div>
    <div class="contact-phone"><svg width="11" height="11" viewBox="0 0 12 12"><circle cx="6" cy="6" r="6" fill="#ffc21a"/><circle cx="6" cy="6" r="2.5" fill="#250805"/></svg>540-555-0147</div>
  </div>
  <div class="divider"></div>
  <div class="contact men">
    <div class="contact-label">PARA HOMBRES</div>
    <div class="contact-phone"><svg width="11" height="11" viewBox="0 0 12 12"><circle cx="6" cy="6" r="6" fill="#ffc21a"/><circle cx="6" cy="6" r="2.5" fill="#250805"/></svg>571-555-0182</div>
  </div>
</div>
</body>
</html>
```